Letterhead and Biz card using my logo
Law Offices of Daniel R. Horvath
Letterhead and Biz card using my logo  - Law
Creative Brief
Professional
The Law Offices of Daniel R. Horvath
41756 County Lane 9 Suite 200 Boca Raton, FL 33517
danielrhorvath@quillpost.net
www.thedebtmender.net
(if you can add this onto the biz card without it looking to busy, use my slogan) "There IS life after bankruptcy."

```html
<!DOCTYPE html>
<html lang="en">
<head>
<meta charset="UTF-8">
<title>Law Offices of Daniel R. Horvath — Business Card</title>
<link href="https://fonts.googleapis.com/css2?family=Open+Sans:ital,wght@1,700&family=Tinos:wght@400;700&display=swap" rel="stylesheet">
<style>
  :root {
    --page-bg: #ecebe8;
    --blue-deep: #123f8c;
    --blue-mid: #1d63b8;
    --blue-light: #3f9be0;
    --white: #ffffff;
    --wood-light: #f1e1c4;
    --wood-mid: #e3cba3;
    --wood-dark: #d6b98c;
    --divider: #9b8a6c;
    --brand-blue: #1c4f9c;
  }
  html, body {
    margin: 0;
    width: 1200px;
    height: 965px;
    overflow: hidden;
    background: var(--page-bg);
  }
  .card {
    position: absolute;
    left: 100px;
    top: 219px;
    width: 1000px;
    height: 527px;
    border-radius: 34px;
    overflow: hidden;
    display: flex;
    box-shadow: 0 6px 18px rgba(0,0,0,0.18);
  }
  .card__info {
    position: relative;
    width: 450px;
    height: 100%;
    background: radial-gradient(ellipse 90% 80% at 75% 55%, var(--blue-light) 0%, var(--blue-mid) 45%, var(--blue-deep) 100%);
    color: var(--white);
    border-right: 3px solid var(--divider);
    box-sizing: border-box;
  }
  .card__brand {
    flex: 1;
    position: relative;
    background: linear-gradient(100deg, var(--wood-mid) 0%, var(--wood-light) 35%, var(--wood-mid) 65%, var(--wood-light) 85%, var(--wood-dark) 100%);
    display: flex;
    align-items: center;
    justify-content: center;
    gap: 22px;
  }
  .person__name, .person__title {
    position: absolute;
    left: 37px;
    margin: 0;
    font-family: "Open Sans", Arial, sans-serif;
    font-style: italic;
    font-weight: 700;
  }
  .person__name { top: 44px; font-size: 31px; }
  .person__title { top: 86px; font-size: 25px; }
  .address {
    position: absolute;
    left: 37px;
    top: 178px;
    margin: 0;
    font-family: "Tinos", "Times New Roman", serif;
    font-style: normal;
    font-size: 25px;
    line-height: 33px;
  }
  .contacts {
    position: absolute;
    left: 37px;
    top: 309px;
    margin: 0;
    padding: 0;
    list-style: none;
    font-family: "Tinos", "Times New Roman", serif;
    font-size: 25px;
  }
  .contacts li {
    display: flex;
    align-items: center;
    height: 33.5px;
  }
  .contacts svg {
    width: 22px;
    height: 22px;
    margin-right: 14px;
    fill: var(--white);
  }
  .brand__mark {
    width: 62px;
    height: 62px;
    border-radius: 50%;
    background: var(--brand-blue);
  }
  .brand__name {
    font-family: "Tinos", "Times New Roman", serif;
    font-weight: 700;
    font-size: 50px;
    color: var(--brand-blue);
  }
</style>
</head>
<body>
  <div class="card">
    <section class="card__info">
      <h1 class="person__name">Your Name</h1>
      <h2 class="person__title">Your Title</h2>
      <address class="address">
        41756 County Lane 9<br>
        Suite 200<br>
        Boca Raton, FL 33517
      </address>
      <ul class="contacts">
        <li>
          <svg viewBox="0 0 24 24" aria-hidden="true"><path d="M6.6 10.8c1.4 2.8 3.8 5.1 6.6 6.6l2.2-2.2c.3-.3.7-.4 1-.2 1.1.4 2.3.6 3.6.6.6 0 1 .4 1 1V20c0 .6-.4 1-1 1C10.6 21 3 13.4 3 4c0-.6.4-1 1-1h3.5c.6 0 1 .4 1 1 0 1.3.2 2.5.6 3.6.1.3 0 .7-.2 1z"/></svg>
          561.555.0144
        </li>
        <li>
          <svg viewBox="0 0 24 24" aria-hidden="true"><path d="M7 1h10c1.1 0 2 .9 2 2v18c0 1.1-.9 2-2 2H7c-1.1 0-2-.9-2-2V3c0-1.1.9-2 2-2zm0 3v13h10V4zm5 15.2a1.2 1.2 0 100 2.4 1.2 1.2 0 000-2.4z"/></svg>
          561.555.0152
        </li>
        <li>
          <svg viewBox="0 0 24 24" aria-hidden="true"><path d="M7 2h8l3 3v5h1c1.1 0 2 .9 2 2v8c0 1.1-.9 2-2 2H5c-1.1 0-2-.9-2-2v-8c0-1.1.9-2 2-2h2zm2 2v6h7V6h-2V4zm-2 10v2h2v-2zm4 0v2h2v-2zm4 0v2h2v-2z"/></svg>
          561.555.0185
        </li>
        <li>
          <svg viewBox="0 0 24 24" aria-hidden="true"><path d="M2 5h20v14H2zm2 2v.4l8 5.2 8-5.2V7zm0 2.8V17h16V9.8l-8 5.2z"/></svg>
          danielrhorvath@quillpost.net
        </li>
        <li>
          <svg viewBox="0 0 24 24" aria-hidden="true"><path d="M12 2a10 10 0 100 20 10 10 0 000-20zm6.9 6h-2.8a15 15 0 00-1.4-3.9A8 8 0 0118.9 8zM12 4c.8 1.2 1.5 2.5 1.9 4h-3.8c.4-1.5 1.1-2.8 1.9-4zM4.3 14a8 8 0 010-4h3.2a17 17 0 000 4zm.8 2h2.8c.3 1.4.8 2.7 1.4 3.9A8 8 0 015.1 16zM7.9 8H5.1a8 8 0 014.2-3.9C8.7 5.3 8.2 6.6 7.9 8zM12 20c-.8-1.2-1.5-2.5-1.9-4h3.8c-.4 1.5-1.1 2.8-1.9 4zm2.3-6H9.7a15 15 0 010-4h4.6a15 15 0 010 4zm.4 5.9c.6-1.2 1.1-2.5 1.4-3.9h2.8a8 8 0 01-4.2 3.9zm1.8-5.9a17 17 0 000-4h3.2a8 8 0 010 4z"/></svg>
          www.thedebtmender.net
        </li>
      </ul>
    </section>
    <section class="card__brand" role="img" aria-label="Light wood grain surface behind the firm name">
      <span class="brand__mark"></span>
      <span class="brand__name">Horvath Law</span>
    </section>
  </div>
</body>
</html>
```